Business Card Design

We need a business card design that can also be aplied for postcards. We are a small indie record company that also do consulting, and development of independat artitst . I already have the name and the basic idea of what i am looking for but i am open to any suggestion.
Info for the card
Name of the company : Velmora Records
NAME : Tomas Invaldi
PHONE : 208-5536142
EMAIL : hello@velmorarecords.example
WEB: www.velmorarecords.example
Target Market(s)
Male - Female independent musicians ages 18 to 45
Industry/Entity Type
Record Company
Contact Information for Business Card
Independant records company that also works in consulting for music business models for independent artists
Look and feel
Each slider illustrates characteristics of the customer's brand and the style your logo design should communicate.

```html
<!DOCTYPE html>
<html lang="en">
<head>
<meta charset="utf-8">
<title>Velmora Records – Business Card</title>
<link rel="stylesheet" href="https://fonts.googleapis.com/css2?family=Stardos+Stencil:wght@700&family=Open+Sans:wght@400&display=swap">
<style>
  :root {
    --page-bg: #ffffff;
    --paper-light: #f4f4f4;
    --paper-dark: #b3b3b3;
    --band-light: #52b1de;
    --band-dark: #2b9bd4;
    --ink: #0c0c0c;
    --contact-ink: #ffffff;
  }
  html, body {
    margin: 0;
    width: 1200px;
    height: 1200px;
    overflow: hidden;
    background: var(--page-bg);
  }
  .canvas {
    position: relative;
    width: 1200px;
    height: 1200px;
  }
  .card {
    position: absolute;
    display: block;
    box-shadow: 0 1px 3px rgba(0,0,0,0.35);
  }
  .card--front { left: 172px; top: 62px; width: 858px; height: 523px; }
  .card--back  { left: 169px; top: 630px; width: 861px; height: 528px; }
  .paper-start { stop-color: var(--paper-light); }
  .paper-end   { stop-color: var(--paper-dark); }
  .band-start  { stop-color: var(--band-light); }
  .band-end    { stop-color: var(--band-dark); }
  .stencil-title {
    font-family: "Stardos Stencil", "Stencil", serif;
    font-weight: 700;
    font-size: 38px;
    letter-spacing: 1px;
    fill: var(--ink);
  }
  .contact-line {
    font-family: "Open Sans", "Segoe UI", sans-serif;
    font-size: 25px;
    fill: var(--contact-ink);
  }
</style>
</head>
<body>
<main class="canvas">

  <svg class="card card--front" viewBox="0 0 858 523" aria-label="Card front">
    <defs>
      <radialGradient id="paperFront" cx="0.45" cy="0.6" r="0.75">
        <stop offset="0.25" class="paper-start"/>
        <stop offset="1" class="paper-end"/>
      </radialGradient>
      <radialGradient id="bandFront" cx="0.45" cy="0.35" r="0.8">
        <stop offset="0" class="band-start"/>
        <stop offset="1" class="band-end"/>
      </radialGradient>
    </defs>
    <rect class="paper" width="858" height="523" fill="url(#paperFront)"/>
    <polygon class="band band--upper" points="405,0 858,0 858,95 501,431 239,157" fill="url(#bandFront)"/>
    <polygon class="band band--lower" points="0,384 165,229 426,503 406,523 0,523" fill="url(#bandFront)"/>
    <text class="stencil-title company-name" x="333" y="335" text-anchor="middle" dominant-baseline="middle" transform="rotate(45 333 335)">VELMORA RECORDS</text>
  </svg>

  <svg class="card card--back" viewBox="0 0 861 528" aria-label="Card back">
    <defs>
      <radialGradient id="paperBack" cx="0.45" cy="0.6" r="0.75">
        <stop offset="0.25" class="paper-start"/>
        <stop offset="1" class="paper-end"/>
      </radialGradient>
      <radialGradient id="bandBack" cx="0.45" cy="0.35" r="0.8">
        <stop offset="0" class="band-start"/>
        <stop offset="1" class="band-end"/>
      </radialGradient>
    </defs>
    <rect class="paper" width="861" height="528" fill="url(#paperBack)"/>
    <polygon class="band band--upper" points="406,0 861,0 861,96 503,435 240,161" fill="url(#bandBack)"/>
    <polygon class="band band--lower" points="0,388 164,232 428,505 406,528 0,528" fill="url(#bandBack)"/>
    <text class="stencil-title person-name" x="331" y="333" text-anchor="middle" dominant-baseline="middle" transform="rotate(45 331 333)">TOMAS INVALDI</text>
    <g class="contact-details">
      <text class="contact-line contact-phone" x="443" y="310" transform="rotate(-45 443 310)">208-5536142</text>
      <text class="contact-line contact-email" x="474" y="335" transform="rotate(-45 474 335)">hello@velmorarecords.example</text>
      <text class="contact-line contact-web" x="503" y="360" transform="rotate(-45 503 360)">www.velmorarecords.example</text>
    </g>
  </svg>

</main>
</body>
</html>
```